Machine shop needs a brochure designed

Would like a tri-fold professional looking brochure that tells about our business and our capabilities. We are a family-owned business with over 50 years of experience in precision manufacturing. We specialize in close-tolerance tooling and serve a diverse array of industries. Our colors are red, black, white, and gray. The final design should make a great impression and spotlight our capabilities and quality.

Target Market(s)

Manufacturing industries needing tooling

Industry/Entity Type

Machining, grinding, manufacturing

Font styles to use
Serif

Colors
EB3D1F
EC4F4E
F09395
F8D3D4
FCEDEE

Requirements
Must have
• Logo, colors are red, black, white, gray
Nice to have
• Images of CNC process or machining/grinding metal parts.

```html
<!DOCTYPE html>
<html lang="en">
<head>
<meta charset="utf-8">
<title>Norvale Tooling – Tri-fold Brochure</title>
<link rel="stylesheet" href="https://fonts.googleapis.com/css2?family=Anton&family=Poppins:ital,wght@0,300;0,400;0,500;0,600;0,700;1,600;1,700&display=swap">
<style>
:root{
  --red:#e8141b;
  --ink:#22253a;
  --ink-deep:#1a1c2c;
  --white:#ffffff;
  --paper:#ffffff;
  --stage:#e7e7e8;
  --text:#2b2b30;
  --muted:#c9cbd6;
  --rule:#8d90a3;
}
*{box-sizing:border-box;margin:0;padding:0}
html,body{width:1200px;height:2941px;overflow:hidden}
body{background:var(--stage);font-family:"Poppins",sans-serif;color:var(--text);position:relative}
.spread{position:absolute;left:50px;width:1100px;height:851px;background:var(--paper);box-shadow:0 10px 30px rgba(0,0,0,.18);overflow:hidden}
.spread--outside{top:570px}
.spread--inside{top:1521px}
.panel{position:absolute;top:0;height:100%}
.panel > *{position:absolute}
.photo{display:block}
.red{color:var(--red)}
.center{text-align:center;left:0;right:0}

/* top red band with teeth */
.band{position:absolute;left:0;top:0;width:733px;height:56px;background:var(--red);z-index:3}
.band-teeth{position:absolute;left:0;top:56px;width:733px;height:10px;z-index:3}

/* name block (replaces mark) */
.namebox{background:var(--red);color:var(--white);font-family:"Poppins",sans-serif;font-weight:700;display:flex;align-items:center;justify-content:center;letter-spacing:.5px}

/* ---------- outside: about panel ---------- */
.about{left:0;width:367px;background:var(--paper)}
.about .photo{left:0;top:56px;width:367px;height:317px;background:linear-gradient(160deg,#5a4636 0%,#2d241d 45%,#6d5a48 80%,#3a3029 100%)}
.flag-pole{left:266px;top:294px;width:3px;height:120px;background:var(--ink)}
.flag{left:270px;top:300px;width:92px;height:58px;font-size:13px;z-index:2}
.about-title{left:23px;top:388px;font-size:25px;font-weight:300;color:var(--ink);letter-spacing:.5px}
.about-title b{font-weight:700;color:var(--red)}
.about-copy{left:23px;top:438px;width:340px;font-size:11.1px;line-height:1.23;color:#333}
.about-copy p{margin-bottom:10px}
.about-copy strong{color:var(--red);font-weight:600}
.specialize{left:28px;top:740px;width:313px;height:130px;background:var(--ink);border:3px solid var(--red);border-radius:10px 10px 0 0;padding:14px 18px;color:var(--white)}
.specialize h3{font-size:16px;font-weight:600;margin-bottom:8px}
.specialize h3 span{color:var(--red)}
.specialize ul{list-style:none;display:flex;gap:16px}
.specialize li{font-size:11.5px;line-height:1.3;display:flex;gap:5px;width:140px}
.tick{flex:none;width:13px;height:13px;margin-top:2px}

/* ---------- outside: contact panel ---------- */
.contact{left:367px;width:366px;background:var(--ink);color:var(--white)}
.contact .bgphoto{left:0;top:56px;width:366px;height:795px;background:radial-gradient(ellipse at 50% 70%,#2e3248 0%,var(--ink) 60%)}
.portrait{left:51px;width:83px;height:83px;border:3px solid var(--red);border-radius:6px;background:linear-gradient(180deg,#9aa0a8,#5b6068)}
.portrait--one{top:103px}
.portrait--two{top:203px}
.person{left:159px;font-size:15px;line-height:1.12;font-weight:500;letter-spacing:.3px}
.person span{display:block;color:var(--red)}
.person-role{left:159px;font-size:11.5px;font-weight:400;letter-spacing:.3px}
.rule{left:0;width:100%;height:1px;background:var(--rule)}
.contact-cta{top:334px;font-size:16px;font-weight:600}
.contact-cta-sub{top:362px;font-size:13px;line-height:1.2;font-weight:400}
.contact-company{top:450px;font-size:17px;font-weight:700;letter-spacing:.2px}
.pill{top:492px;left:119px;width:128px;height:24px;border-radius:12px;background:var(--white);color:var(--red);font-size:13px;font-weight:600;display:flex;align-items:center;justify-content:center}
.icon{width:20px;height:20px}
.phone-1{left:107px;top:548px}
.phone-2{left:246px;top:548px}
.num{top:571px;font-size:13px}
.num--one{left:68px}
.num--two{left:209px}
.dash{left:182px;top:546px;height:48px;border-left:1.5px dashed var(--muted)}
.pin{left:173px;top:596px}
.addr{top:619px;font-size:13px;line-height:1.2}
.mail{top:686px;font-size:13px}
.globe{left:173px;top:716px}
.web{top:743px;font-size:13px}
.tagline{left:50px;top:777px;width:316px;height:49px;background:var(--red);font-size:18px;line-height:1.05;display:flex;align-items:center;justify-content:center;text-align:center}

/* ---------- outside: cover panel ---------- */
.cover{left:733px;width:367px;background:var(--paper)}
.cover .dark{left:0;top:0;width:367px;height:540px;background:var(--ink-deep);clip-path:polygon(0 0,100% 0,100% 460px,50% 538px,0 460px)}
.cover .namebox{left:98px;top:25px;width:172px;height:69px;font-size:18px}
.cover-company{top:105px;font-size:17px;font-weight:700;color:var(--white);letter-spacing:.2px}
.cover .photo{left:0;top:134px;width:367px;height:394px;background:linear-gradient(170deg,#6b5a4a 0%,#3a3129 40%,#8c7760 70%,#2b241e 100%);clip-path:polygon(0 0,100% 0,100% 316px,50% 392px,0 316px)}
.welcome{top:548px;font-family:"Anton",sans-serif;font-size:44px;line-height:1.04;color:var(--ink-deep);letter-spacing:.5px}
.welcome span{display:block}
.cover-copy{left:32px;right:32px;top:706px;text-align:center;font-size:10.4px;line-height:1.3;color:#444}
.url-bar{left:44px;top:800px;width:278px;height:25px;background:var(--red);color:var(--white);font-size:14px;font-weight:600;display:flex;align-items:center;justify-content:center}

/* ---------- inside: capabilities ---------- */
.caps{left:0;width:367px;background:var(--paper)}
.caps-bar{left:0;top:23px;width:367px;height:49px;background:var(--red);color:var(--white);font-size:22px;font-weight:400;padding-left:23px;display:flex;align-items:center;letter-spacing:.2px}
.caps-bar b{font-weight:700;margin-left:6px}
.caps-intro{left:23px;top:96px;width:330px;font-size:19px;line-height:1.05;color:var(--ink-deep)}
.caps-intro b{color:var(--red);font-weight:700}
.caps-intro small{display:block;font-size:14px;font-weight:500;margin-top:6px}
.caps .photo{left:0;top:177px;width:367px;height:351px;background:radial-gradient(circle at 30% 45%,#c9d0d8 0%,#7f8a96 25%,#34506e 60%,#1f2f45 100%)}
.caps-head{left:23px;top:555px;font-size:15.5px;font-weight:600;color:var(--ink-deep)}
.caps-head span{color:var(--red)}
.caps-rule{left:23px;top:582px;width:322px;height:1px;background:#9a9a9a}
.caps-list{list-style:none;top:603px;font-size:12px;line-height:1.25;color:#333}
.caps-list li{display:flex;gap:8px;margin-bottom:10px}
.caps-list .tick{margin-top:1px}
.caps-list--left{left:23px;width:160px}
.caps-list--right{left:190px;width:160px}
.caps-list em{font-style:normal;font-weight:600}

/* ---------- inside: gallery ---------- */
.gallery{left:367px;width:366px;background:var(--paper)}
.frame{left:25px;width:314px;height:237px;border:4px solid var(--red);border-radius:8px}
.frame--one{top:25px;background:linear-gradient(135deg,#4a5a44 0%,#8b8f7a 40%,#c8b64a 55%,#3d4a3a 100%)}
.frame--two{top:282px;background:radial-gradient(circle at 50% 55%,#7d8598 0%,#2a2f45 45%,#12141f 100%)}
.gallery-caption{top:560px;font-size:12px;font-weight:600;line-height:1.15;color:#222}
.gallery .tools{left:10px;top:602px;width:317px;height:200px;background:radial-gradient(ellipse at 45% 55%,#d9dce2 0%,#f4f4f6 55%,#ffffff 80%)}
.url-tab{position:absolute;left:523px;top:805px;width:240px;height:20px;z-index:4}
.url-tab span{position:absolute;inset:0;display:flex;align-items:center;justify-content:center;color:var(--white);font-size:12px;font-weight:500;padding-right:10px}

/* ---------- inside: back panel ---------- */
.back{left:733px;width:367px;background:var(--ink-deep);color:var(--white)}
.back-teeth{position:absolute;left:723px;top:0;width:10px;height:851px;z-index:2}
.back-rule{left:0;width:100%;height:1px;background:var(--rule)}
.back-lead{left:40px;top:40px;width:315px;font-size:14.5px;line-height:1.25;font-weight:700;font-style:italic}
.back-lead span{color:var(--red)}
.back .photo{left:0;top:127px;width:367px;height:532px;background:radial-gradient(circle at 20% 20%,#8a7a63 0%,transparent 22%),radial-gradient(circle at 70% 35%,#7b6c58 0%,transparent 22%),radial-gradient(circle at 40% 70%,#6e604f 0%,transparent 24%),linear-gradient(180deg,#3a3a46 0%,#242634 100%)}
.back-title{left:44px;top:680px;font-size:50px;font-weight:300;line-height:1.12;letter-spacing:1px}
</style>
</head>
<body>

<!-- Outside spread -->
<section class="spread spread--outside" aria-label="Brochure outside">
  <div class="band"></div>
  <svg class="band-teeth" viewBox="0 0 733 10" preserveAspectRatio="none" aria-hidden="true">
    <defs><pattern id="teeth-down" width="14" height="10" patternUnits="userSpaceOnUse"><polygon points="0,0 14,0 7,10" fill="#e8141b"/></pattern></defs>
    <rect width="733" height="10" fill="url(#teeth-down)"/>
  </svg>

  <div class="panel about">
    <div class="photo" role="img" aria-label="Drill bit boring into metal with chips on a workbench"></div>
    <div class="flag-pole"></div>
    <div class="flag namebox">NORVALE</div>
    <h2 class="about-title">ABOUT <b>US</b></h2>
    <div class="about-copy">
      <p><strong>Norvale Tooling, Inc.</strong> is a privately owned company with over fifty years of experience in precision manufacturing. Products manufactured include components for the air-defense missile during Operation Desert Storm, machine gun barrels, close tolerance can tooling, conveyor slats and rollers, molds, various production tooling for several national industries, pump housings for the gasoline industry, aviation and automotive manufacturing, and various precision machining and grinding jobs.</p>
      <p>Currently, Norvale Tooling, Inc. is working with a group of physicians to develop and patent various surgical devices for use in Orthopedic and General Vascular surgeries.</p>
      <p>We at Norvale Tooling, Inc. look forward to the opportunity to work with you and quote any projects you might want us to look at. We take a <strong>“Quality first”</strong> approach to all of our jobs and we have the determination to get the job done according to our clients’ timelines. We are always looking for opportunities to form new alliances and friendships with prospective clients.</p>
    </div>
    <div class="specialize">
      <h3>We <span>Specialize in</span></h3>
      <ul>
        <li><svg class="tick" viewBox="0 0 14 14"><path d="M1 7.5 5 11.5 13 2.5" fill="none" stroke="#e8141b" stroke-width="2.6"/></svg>Close-Tolerance Tooling</li>
        <li><svg class="tick" viewBox="0 0 14 14"><path d="M1 7.5 5 11.5 13 2.5" fill="none" stroke="#e8141b" stroke-width="2.6"/></svg>Serve a Diverse Array of Industries.</li>
      </ul>
    </div>
  </div>

  <div class="panel contact">
    <div class="bgphoto" role="img" aria-label="Dim machining spindle in a dark workshop"></div>
    <div class="portrait portrait--one" role="img" aria-label="Portrait of the president"></div>
    <p class="person" style="top:106px">MARTIN<span>R. CALDWELL</span></p>
    <p class="person-role" style="top:165px">PRESIDENT | SHOP MANAGER</p>
    <div class="portrait portrait--two" role="img" aria-label="Portrait of the chief operating officer"></div>
    <p class="person" style="top:214px">DANIEL<span>CALDWELL</span></p>
    <p class="person-role" style="top:266px">COO</p>
    <div class="rule" style="top:323px"></div>
    <p class="contact-cta center">Contact Us <span class="red">Today</span></p>
    <p class="contact-cta-sub center">and let us help you make your<br>product a success!</p>
    <div class="rule" style="top:405px"></div>
    <p class="contact-company center">NORVALE TOOLING, INC.</p>
    <div class="pill">CONTACT US</div>
    <svg class="icon phone-1" viewBox="0 0 24 24"><path d="M6.6 2.5 9.4 6 7.8 8.3c1.2 2.8 3.1 4.7 5.9 5.9L16 12.6l3.5 2.8-1.6 3.6C10.6 19 5 13.4 3 6.1z" fill="#e8141b"/></svg>
    <svg class="icon phone-2" viewBox="0 0 24 24"><rect x="6" y="3" width="12" height="6" fill="#e8141b"/><rect x="2" y="9" width="20" height="9" rx="2" fill="#e8141b"/><rect x="6" y="15" width="12" height="6" fill="#fff" stroke="#e8141b" stroke-width="2"/></svg>
    <div class="dash"></div>
    <p class="num num--one">555.014.2201</p>
    <p class="num num--two">555.014.2202</p>
    <svg class="icon pin" viewBox="0 0 24 24"><path d="M12 2a7 7 0 0 0-7 7c0 5 7 13 7 13s7-8 7-13a7 7 0 0 0-7-7zm0 9.5A2.5 2.5 0 1 1 12 6.5a2.5 2.5 0 0 1 0 5z" fill="#e8141b"/></svg>
    <p class="addr center">418 Ridgeline Mill Road<br>Oakport, TN 37000</p>
    <p class="mail center">info@norvaletooling.example</p>
    <svg class="icon globe" viewBox="0 0 24 24"><circle cx="12" cy="12" r="9" fill="none" stroke="#e8141b" stroke-width="2.2"/><ellipse cx="12" cy="12" rx="4" ry="9" fill="none" stroke="#e8141b" stroke-width="2"/><path d="M3 12h18M5 7h14M5 17h14" stroke="#e8141b" stroke-width="1.8"/></svg>
    <p class="web center">www.norvaletooling.example</p>
    <div class="tagline">Precise, High-quality<br>Components</div>
  </div>

  <div class="panel cover">
    <div class="dark"></div>
    <div class="namebox">NORVALE</div>
    <p class="cover-company center">NORVALE TOOLING, INC.</p>
    <div class="photo" role="img" aria-label="Machinist in hard hat and safety glasses operating a drill press"></div>
    <h1 class="welcome center"><span>WELCOME TO</span><span class="red">NORVALE</span><span>TOOLING, INC.</span></h1>
    <p class="cover-copy">When your project or process requires precise, high-quality parts or components, look no further than Norvale. We welcome the opportunity to quote your project, and with 40 years combined experience in precision manufacturing, you can rest assured that jobs placed with us will be done to your satisfaction, every time.</p>
    <div class="url-bar">www.norvaletooling.example</div>
  </div>
</section>

<!-- Inside spread -->
<section class="spread spread--inside" aria-label="Brochure inside">
  <div class="panel caps">
    <h2 class="caps-bar">NORVALE<b>CAPABILITIES</b></h2>
    <p class="caps-intro">We at <b>Norvale Offer</b> a wide variety of services<small>to meet your machining &amp; tooling needs</small></p>
    <div class="photo" role="img" aria-label="Close-up of a CNC lathe chuck holding a gold-coated drill bit"></div>
    <h3 class="caps-head">Our <span>Capabilities include</span></h3>
    <div class="caps-rule"></div>
    <ul class="caps-list caps-list--left">
      <li><svg class="tick" viewBox="0 0 14 14"><path d="M1 7.5 5 11.5 13 2.5" fill="none" stroke="#e8141b" stroke-width="2.6"/></svg>Soft Cutting</li>
      <li><svg class="tick" viewBox="0 0 14 14"><path d="M1 7.5 5 11.5 13 2.5" fill="none" stroke="#e8141b" stroke-width="2.6"/></svg>Hard Cutting</li>
      <li><svg class="tick" viewBox="0 0 14 14"><path d="M1 7.5 5 11.5 13 2.5" fill="none" stroke="#e8141b" stroke-width="2.6"/></svg>CNC Machining</li>
      <li><svg class="tick" viewBox="0 0 14 14"><path d="M1 7.5 5 11.5 13 2.5" fill="none" stroke="#e8141b" stroke-width="2.6"/></svg>CNC Milling</li>
      <li><svg class="tick" viewBox="0 0 14 14"><path d="M1 7.5 5 11.5 13 2.5" fill="none" stroke="#e8141b" stroke-width="2.6"/></svg><span>Grinding- O.D./ I.D. and Surface/Rotary <em>(Carbide, Steel, etc.)</em></span></li>
      <li><svg class="tick" viewBox="0 0 14 14"><path d="M1 7.5 5 11.5 13 2.5" fill="none" stroke="#e8141b" stroke-width="2.6"/></svg>0-2 Micro-Finishing</li>
      <li><svg class="tick" viewBox="0 0 14 14"><path d="M1 7.5 5 11.5 13 2.5" fill="none" stroke="#e8141b" stroke-width="2.6"/></svg>Light fabrication</li>
    </ul>
    <ul class="caps-list caps-list--right">
      <li><svg class="tick" viewBox="0 0 14 14"><path d="M1 7.5 5 11.5 13 2.5" fill="none" stroke="#e8141b" stroke-width="2.6"/></svg><span>Conveyor assemblies <em>- slats, rollers, etc.</em></span></li>
      <li><svg class="tick" viewBox="0 0 14 14"><path d="M1 7.5 5 11.5 13 2.5" fill="none" stroke="#e8141b" stroke-width="2.6"/></svg><span>Can tooling- Trimmer Knives, Knockouts, Punch Bolts, Printer Mandrels, Cut Edges, Blank &amp; Draw Dies, etc</span></li>
      <li><svg class="tick" viewBox="0 0 14 14"><path d="M1 7.5 5 11.5 13 2.5" fill="none" stroke="#e8141b" stroke-width="2.6"/></svg><span>Wide range of Aerospace and Automotive tooling</span></li>
      <li><svg class="tick" viewBox="0 0 14 14"><path d="M1 7.5 5 11.5 13 2.5" fill="none" stroke="#e8141b" stroke-width="2.6"/></svg><span>NAICS 332813, 332721 &amp; 333512</span></li>
    </ul>
  </div>

  <div class="panel gallery">
    <div class="frame frame--one" role="img" aria-label="Worker in yellow hard hat and ear protection at a milling machine"></div>
    <div class="frame frame--two" role="img" aria-label="End mill cutting metal with chips flying"></div>
    <p class="gallery-caption center">Professional cutting tools set<br>consists of drill and<br>Imaterial Carbide used for metalwork</p>
    <div class="tools" role="img" aria-label="Tool holder, drill bit and carbide inserts on white"></div>
  </div>

  <div class="url-tab">
    <svg width="240" height="20" viewBox="0 0 240 20" aria-hidden="true"><polygon points="0,0 228,0 240,10 228,20 0,20" fill="#e8141b"/></svg>
    <span>www.norvaletooling.example</span>
  </div>

  <svg class="back-teeth" viewBox="0 0 10 851" preserveAspectRatio="none" aria-hidden="true">
    <defs><pattern id="teeth-left" width="10" height="14" patternUnits="userSpaceOnUse"><polygon points="10,0 10,14 0,7" fill="#1a1c2c"/></pattern></defs>
    <rect width="10" height="851" fill="url(#teeth-left)"/>
  </svg>

  <div class="panel back">
    <div class="back-rule" style="top:22px"></div>
    <p class="back-lead">We are a family-owned business with over <span>50 years of experience in precision manufacturing.</span></p>
    <div class="back-rule" style="top:117px"></div>
    <div class="photo" role="img" aria-label="Stacked ends of polished steel tubes"></div>
    <div class="back-rule" style="top:665px"></div>
    <h2 class="back-title">MACHINE<br>SHOP</h2>
    <div class="back-rule" style="top:795px"></div>
  </div>
</section>

</body>
</html>
```